Consultancy Business Card Design

We need a business card design for a new company based in singapore called FortyOne. FortyOne a boutique consultancy firm offering broad-based business solutions, from conception to re-invention, for ventures from new start-ups to long-running traditional businesses.
Its 2 main divisions (Food & Beverage Operations and Construction & Project Management) have access to a wide range of networks, knowledge bases, and resources to service its clients across numerous diverse sectors. This includes, and is not limited to, construction, F&B, and retail.
We are a company that combines the ambition, boldness and energy of one in the 20s with the dedication, level-headedness and dependability of one entering its 30s. Bridging the experiences of the old with ideals of the young, we draw on the positives of both to create a unique synergy.
We hope to see designs that fits our company profile.
Boutique
FortyOne(Company Name)
Marcus Leow (Name)
Principle Consultant (Title)
F&B and Hospitality (Division)
(+65) 8364 5170 (Contact no.)
marcus@fortyone-example.com.sg (Email)

```html
<!DOCTYPE html>
<html lang="en">
<head>
<meta charset="utf-8">
<title>FortyOne – Business Card</title>
<link rel="stylesheet" href="https://fonts.googleapis.com/css2?family=Josefin+Sans:wght@400;600&display=swap">
<style>
  :root {
    --backdrop: #e9e6e1;
    --card-black: #1d1d1f;
    --card-edge: #2a2a2c;
    --brand-red: #e3262f;
    --brand-grey: #7a7a7c;
    --text-white: #f2f2f2;
    --text-soft: #cfcfcf;
  }
  * { margin: 0; padding: 0; box-sizing: border-box; }
  html, body { width: 1200px; height: 900px; overflow: hidden; }
  body {
    background: var(--backdrop);
    font-family: "Josefin Sans", sans-serif;
    display: flex;
    align-items: center;
    justify-content: center;
    gap: 80px;
  }
  .card {
    position: relative;
    width: 500px;
    height: 300px;
    background: linear-gradient(135deg, var(--card-edge), var(--card-black) 60%);
    border-radius: 4px;
    box-shadow: 0 14px 30px rgba(0,0,0,0.28);
    overflow: hidden;
  }
  .card-front {
    display: flex;
    align-items: center;
    justify-content: center;
  }
  .brand-name {
    display: flex;
    align-items: center;
    gap: 12px;
    font-weight: 600;
    letter-spacing: 0.02em;
  }
  .brand-dot {
    width: 22px;
    height: 22px;
    border-radius: 50%;
  }
  .card-front .brand-name { font-size: 48px; color: var(--brand-red); }
  .card-front .brand-dot { background: var(--brand-red); width: 30px; height: 30px; }
  .card-back .brand-name {
    position: absolute;
    left: 40px;
    top: 176px;
    font-size: 34px;
    color: var(--brand-grey);
  }
  .card-back .brand-dot { background: var(--brand-grey); }
  .contact-block {
    position: absolute;
    left: 262px;
    top: 56px;
    color: var(--text-soft);
  }
  .person-name {
    font-size: 21px;
    font-weight: 600;
    letter-spacing: 0.06em;
    color: var(--text-white);
    text-transform: uppercase;
    margin-bottom: 6px;
  }
  .person-role, .person-division { font-size: 15px; line-height: 1.3; }
  .contact-list { list-style: none; margin-top: 16px; font-size: 14px; }
  .contact-list li { display: flex; align-items: center; gap: 8px; line-height: 1.6; }
  .contact-icon { width: 12px; height: 12px; fill: var(--brand-red); flex: none; }
</style>
</head>
<body>
  <section class="card card-front" aria-label="Card front">
    <div class="brand-name"><span class="brand-dot"></span>FortyOne</div>
  </section>

  <section class="card card-back" aria-label="Card back">
    <div class="brand-name"><span class="brand-dot"></span>FortyOne</div>
    <div class="contact-block">
      <h1 class="person-name">Marcus Leow</h1>
      <p class="person-role">Principle Consultant</p>
      <p class="person-division">F&amp;B and Hospitality</p>
      <ul class="contact-list">
        <li>
          <svg class="contact-icon" viewBox="0 0 24 24" aria-hidden="true"><path d="M6.6 10.8a15.1 15.1 0 0 0 6.6 6.6l2.2-2.2a1 1 0 0 1 1-.25 11.4 11.4 0 0 0 3.6.57 1 1 0 0 1 1 1V20a1 1 0 0 1-1 1A17 17 0 0 1 3 4a1 1 0 0 1 1-1h3.5a1 1 0 0 1 1 1c0 1.25.2 2.45.57 3.6a1 1 0 0 1-.25 1z"/></svg>
          (+65) 8364 5170
        </li>
        <li>
          <svg class="contact-icon" viewBox="0 0 24 24" aria-hidden="true"><path d="M2 5h20v14H2z M2 5l10 8 10-8" /></svg>
          marcus@fortyone-example.com.sg
        </li>
      </ul>
    </div>
  </section>
</body>
</html>
```